PelloranDesk Postcard Campaign

We need a postcard design for our company, PelloranDesk.com - we are a job board for mechanics and auto technicians. We are sending a postcard to 1000 auto shops and trucking companies across the US to try to get them to come to our website and purchase a job pack and post a job posting. We will be offering them a promotion of "Save $20 on your first job post. Enter 'SUMMER20' at checkout."

We would like to see designs that are consistent with our website theme. The final design should communicate:
- Access to a targeted and local audience of only auto and truck mechanics and technicians
- Search 50,000 resumes
- Money back guarantee

Target Market(s)

Auto mechanic shops, car dealerships looking for mechanics, truck fleet management looking for technicians

Industry/Entity Type

It Company

Font styles to use
Sans Serif

Colors
0392cd
ec1f27
1b1b1b
cbcbcb
ffffff
3277b5

Requirements
Must have
• See content/copy upload
• - Match website color scheme and look and feel
Should not have
• No photos that look like stock photos - preferably steer away from photos unless it looks great

```html
<!DOCTYPE html>
<html lang="en">
<head>
<meta charset="utf-8">
<title>PelloranDesk Postcard</title>
<link rel="stylesheet" href="https://fonts.googleapis.com/css2?family=Roboto+Condensed:wght@300;400;700;800&display=swap">
<style>
  :root {
    --ink: #1b1b1b;
    --paper: #ffffff;
    --brand-blue: #3277b5;
    --sky: #0392cd;
    --cyan-text: #3db4e8;
    --navy: #253a78;
    --navy-edge: #3c5596;
    --deep: #1c3d86;
    --red: #ec1f27;
    --red-fold: #8e1b1e;
    --silver: #cbcbcb;
    --emblem-light: #3ab3ec;
    --emblem-mid: #1f78c8;
  }
  * { margin: 0; padding: 0; box-sizing: border-box; }
  html, body { width: 1200px; height: 930px; overflow: hidden; background: var(--paper); }
  body { font-family: "Roboto Condensed", "Arial Narrow", sans-serif; }

  .postcard { position: relative; width: 1200px; height: 930px; }
  .card-art, .emblem-area { position: absolute; left: 0; top: 0; }

  .headline {
    position: absolute; left: 115px; top: 73px; width: 970px; height: 122px;
    display: flex; align-items: center; justify-content: center;
    color: var(--paper); font-weight: 300; font-size: 64px; letter-spacing: -0.8px;
  }

  .benefits { position: absolute; left: 115px; top: 240px; width: 600px; list-style: none; }
  .benefit {
    position: relative; padding-left: 72px;
    color: var(--paper); font-size: 26px; line-height: 35px; margin-bottom: 25px;
  }
  .benefit::before {
    content: ""; position: absolute; left: 5px; top: 50%; transform: translateY(-50%);
    width: 30px; height: 30px; border-radius: 50%; background: var(--paper);
  }

  .contact { position: absolute; left: 128px; top: 580px; color: var(--paper); font-weight: 800; }
  .contact-site { display: flex; align-items: center; gap: 30px; font-size: 51px; letter-spacing: 0.3px; height: 66px; }
  .contact-site::after {
    content: ""; width: 92px; height: 92px; border-radius: 50%; background: var(--paper);
  }
  .contact-phone { font-size: 40px; margin: 10px 0 0 90px; letter-spacing: 0.5px; font-weight: 700; }

  .footer-band {
    position: absolute; left: 30px; top: 815px; width: 1140px;
    text-align: center; color: var(--cyan-text); font-size: 27px; line-height: 35px;
  }
</style>
</head>
<body>
<main class="postcard">
  <svg class="card-art" width="1200" height="930" viewBox="0 0 1200 930" aria-hidden="true">
    <defs>
      <radialGradient id="panel-glow" cx="420" cy="430" r="760" gradientUnits="userSpaceOnUse">
        <stop offset="0" stop-color="#3a92d2"/>
        <stop offset="0.55" stop-color="#2b63ad"/>
        <stop offset="1" stop-color="var(--deep)"/>
      </radialGradient>
      <linearGradient id="footer-shade" x1="0" y1="0" x2="0" y2="1">
        <stop offset="0" stop-color="#2a2a2a"/>
        <stop offset="1" stop-color="#111111"/>
      </linearGradient>
    </defs>
    <rect class="frame" x="30" y="30" width="1140" height="870" fill="var(--ink)"/>
    <rect class="panel" x="30" y="128" width="1140" height="657" fill="url(#panel-glow)"/>
    <polygon class="corner-red" points="30,520 30,785 160,785" fill="var(--red)"/>
    <polygon class="corner-stripe" points="30,495 30,520 168,785 186,785" fill="#9aa3c6"/>
    <rect class="footer" x="30" y="785" width="1140" height="115" fill="url(#footer-shade)"/>
    <polygon class="fold-left" points="115,73 240,40 240,73" fill="var(--red-fold)"/>
    <polygon class="fold-right" points="958,195 1085,195 958,228" fill="var(--red-fold)"/>
    <rect class="title-band" x="115" y="73" width="970" height="122" fill="var(--navy)" stroke="var(--navy-edge)" stroke-width="2"/>
  </svg>

  <svg class="emblem-area" width="1200" height="930" viewBox="0 0 1200 930" role="img" aria-label="Large decorative brand emblem in bright blue tones">
    <defs>
      <radialGradient id="emblem-tone" cx="0.3" cy="0.5" r="0.8">
        <stop offset="0" stop-color="var(--emblem-light)"/>
        <stop offset="0.6" stop-color="var(--emblem-mid)"/>
        <stop offset="1" stop-color="var(--emblem-mid)" stop-opacity="0.6"/>
      </radialGradient>
    </defs>
    <rect x="724" y="228" width="446" height="557" fill="url(#emblem-tone)"/>
  </svg>

  <h1 class="headline">FIND YOUR NEXT MECHANIC TODAY!</h1>

  <ul class="benefits">
    <li class="benefit">Post a job with us and get access to hundreds of qualified technicians in your area.</li>
    <li class="benefit">Includes distribution and promotion across multiple job boards, such as Hireloom.com, JobQuarry, Vantaboard.com etc.</li>
    <li class="benefit">Search 50,000+ resumes, with new candidates added daily.</li>
  </ul>

  <div class="contact">
    <p class="contact-site">PELLORANDESK.COM</p>
    <p class="contact-phone">(800) 555-0142</p>
  </div>

  <footer class="footer-band">
    <p>CONNECTING AUTOMOTIVE EMPLOYERS WITH QUALIFIED TECHNICIANS SINCE 2006</p>
    <p>100% SATISFACTION GUARANTEED, OR YOUR MONEY BACK</p>
  </footer>
</main>
</body>
</html>
```